Corporate Word-document templates

We need these documents templates for the following types of documentation:

- Proposal
- Report (meetings)
- Solution description (technical)
- Documentation

The front page of the documents can take inspiration from our PowerPoint template, website (https://www.lindqor.com/) and brand book. It should reflect our new branding guidelines.

See attached documents for structure and what we need them to contain. We need:
- front page
- generalt tekst page after the front page
- table of contents
- logo in upper right corner, page number + info in the footer, structure of tables
- anything else?

1) Make a design suggestion for the front page of the proposal and the Documentation
2) When we agree on the structure and front page, make the other two documents
3) we need all four documents with four different logos. 4 x 4 documents. the logos are: Marvelund, MVL, MVL Horizon & MVL Lens.

Target Market(s)

Large and medium corporations. Roles such as CEO, CFO, CIO, CTO, Controllers, Analysts, leaders/managers

Industry/Entity Type

Information Technology

Font styles to use
Sans Serif

Requirements
Must have
• - elements that are key to a word template
- four different word template files - each with the four different logos
- chose colors from our brand book

```html
<!DOCTYPE html>
<html lang="en">
<head>
<meta charset="utf-8">
<title>Marvelund – Word Template Pages</title>
<link rel="stylesheet" href="https://fonts.googleapis.com/css2?family=Source+Sans+3:wght@400;600;700;800&display=swap">
<style>
:root{
  --navy:#0c2746;
  --navy-2:#143d66;
  --blue:#1f5f96;
  --teal:#2a8fb8;
  --sky:#d6e8f3;
  --yellow:#f2b41c;
  --orange:#ee8a23;
  --ink:#2b3440;
  --grey:#8a94a0;
  --line:#c9d2db;
  --board:#ffffff;
}
*{box-sizing:border-box;margin:0;padding:0}
html,body{width:857px;height:1200px;overflow:hidden;background:var(--board);font-family:"Source Sans 3",Arial,sans-serif;color:var(--ink)}
.board{position:relative;width:857px;height:1200px}
.page{position:absolute;width:230px;height:320px;background:#fff;box-shadow:0 1px 4px rgba(0,0,0,.28);overflow:hidden}
.page-label{position:absolute;width:230px;text-align:center;font-size:11px;letter-spacing:.5px;color:#333}
/* header & footer */
.page-header{position:absolute;top:10px;left:0;right:0;height:18px}
.header-bar{position:absolute;left:0;top:0;width:150px;height:18px;background:var(--navy);color:#fff;font-size:7px;font-weight:700;line-height:18px;padding-left:12px}
.header-accent{position:absolute;left:150px;top:0;width:14px;height:18px;background:var(--yellow);clip-path:polygon(0 0,40% 0,100% 100%,60% 100%)}
.brand{font-weight:800;color:var(--navy);display:flex;align-items:center;gap:3px}
.brand-dot{width:5px;height:5px;background:var(--yellow)}
.page-header .brand{position:absolute;right:10px;top:3px;font-size:9px}
.page-footer{position:absolute;bottom:10px;left:12px;right:12px;height:12px;border-top:.6px solid var(--line);display:flex;justify-content:space-between;align-items:flex-end;font-size:4px;color:var(--grey)}
.page-footer .brand{font-size:6px}
.content{position:absolute;top:38px;left:14px;right:14px;font-size:4px;line-height:5.6px;color:var(--ink)}
.content h2{font-size:7px;color:var(--navy);font-weight:700;margin:4px 0 3px}
.content h3{font-size:5.5px;color:var(--blue);font-weight:700;margin:4px 0 2px}
.content p{margin-bottom:3px}
.content ul{margin:0 0 3px 8px}
.note{border-left:2px solid var(--yellow);padding-left:4px;font-style:normal;color:var(--blue)}
/* toc */
.toc-row{display:flex;font-size:4.4px;line-height:7px}
.toc-row .fill{flex:1;border-bottom:.5px dotted var(--grey);margin:0 2px 2px}
.toc-row.main{font-weight:700;color:var(--navy)}
.toc-row.sub{padding-left:6px}
/* tables */
.data-table{width:100%;border-collapse:collapse;font-size:3.8px;margin-bottom:5px}
.data-table th{background:var(--navy);color:#fff;text-align:left;padding:1.5px 2px;font-weight:600}
.data-table td{padding:1.5px 2px;border-bottom:.5px solid var(--line)}
.data-table tr:nth-child(even) td{background:#eef4f9}
/* cover */
.cover-top{position:absolute;inset:0 0 125px 0;background:linear-gradient(160deg,var(--navy-2),var(--navy) 70%)}
.cover-visual{position:absolute;left:80px;top:14px;width:140px;height:92px;background:linear-gradient(135deg,#dfe7ee,#8ea4b8);border-radius:2px}
.cover-title{position:absolute;left:14px;top:122px;color:#fff;font-size:12px;font-weight:600;line-height:14px}
.cover-mid{position:absolute;left:0;right:0;top:195px;height:75px;background:linear-gradient(90deg,#fff 35%,var(--sky))}
.cover-meta{position:absolute;right:14px;top:12px;font-size:5px;line-height:7.5px;color:var(--navy);text-align:left}
.cover-brand{position:absolute;left:14px;bottom:18px;font-size:22px}
.cover-brand .brand-dot{width:10px;height:10px}
/* thanks */
.thanks-top{position:absolute;inset:0 0 105px 0;background:linear-gradient(170deg,var(--blue),var(--navy) 80%)}
.thanks-title{position:absolute;left:14px;top:22px;color:#fff;font-size:12px;font-weight:700}
.offices{position:absolute;left:14px;top:46px;color:#fff;font-size:4.4px;line-height:6px}
.offices h4{font-size:8px;color:var(--yellow);margin-bottom:6px}
.office{margin-bottom:6px}
.office b{font-size:5px}
.thanks-brands{position:absolute;left:14px;right:14px;bottom:34px;display:flex;align-items:center;justify-content:space-between}
.thanks-brands .brand{font-size:18px}
.partner-badge{width:44px;height:18px;background:#e6ebf0}
/* back */
.back{background:linear-gradient(200deg,var(--teal) 0%,var(--blue) 35%,var(--navy) 85%)}
.section-break{position:absolute;left:14px;top:205px;color:#fff}
.section-break .rule{width:32px;height:2px;background:var(--yellow);margin-bottom:5px}
.section-break h1{font-size:11px;font-weight:800;letter-spacing:.3px}
.section-break p{font-size:4.4px;line-height:6px;width:190px;margin-top:4px;color:#d6e6f2}
.chart{display:block;margin:2px 0 4px}
</style>
</head>
<body>
<div class="board">

  <!-- Cover -->
  <section class="page" style="left:45px;top:18px">
    <div class="cover-top"></div>
    <div class="cover-visual" role="img" aria-label="Laptop showing a planning dashboard"></div>
    <div class="cover-title">Administrative revision<br>Input planning</div>
    <div class="cover-mid">
      <div class="cover-meta">Client: Nordvik AS<br>Contact: Anna Holm<br>Date: 01.09.2024<br>Version: 1.0</div>
    </div>
    <div class="brand cover-brand"><span>Marvelund</span><span class="brand-dot"></span></div>
  </section>
  <div class="page-label" style="left:45px;top:350px">COVER PAGE</div>

  <!-- Page 01 TOC -->
  <section class="page" style="left:313px;top:18px">
    <header class="page-header"><div class="header-bar">Project Heading Here</div><div class="header-accent"></div><div class="brand"><span>Marvelund</span></div></header>
    <div class="content">
      <h2>Contents</h2>
      <div class="toc-row main"><span>1 Introduction</span><span class="fill"></span><span>3</span></div>
      <div class="toc-row sub"><span>1.1 Background</span><span class="fill"></span><span>3</span></div>
      <div class="toc-row sub"><span>1.2 Scope</span><span class="fill"></span><span>3</span></div>
      <div class="toc-row sub"><span>1.3 Goals</span><span class="fill"></span><span>4</span></div>
      <div class="toc-row main"><span>2 Solution</span><span class="fill"></span><span>5</span></div>
      <div class="toc-row sub"><span>2.1 Overview</span><span class="fill"></span><span>5</span></div>
      <div class="toc-row sub"><span>2.2 Architecture</span><span class="fill"></span><span>6</span></div>
      <div class="toc-row sub"><span>2.3 Integration</span><span class="fill"></span><span>7</span></div>
      <div class="toc-row sub"><span>2.4 Security</span><span class="fill"></span><span>8</span></div>
      <div class="toc-row main"><span>3 Delivery</span><span class="fill"></span><span>9</span></div>
      <div class="toc-row sub"><span>3.1 Plan</span><span class="fill"></span><span>9</span></div>
      <div class="toc-row sub"><span>3.2 Resources</span><span class="fill"></span><span>10</span></div>
      <div class="toc-row main"><span>4 Pricing</span><span class="fill"></span><span>11</span></div>
      <div class="toc-row main"><span>5 Appendix</span><span class="fill"></span><span>12</span></div>
    </div>
    <footer class="page-footer"><span>MVL Template · Document info · Page 1</span><span class="brand">Marvelund</span></footer>
  </section>
  <div class="page-label" style="left:313px;top:350px">PAGE - 01</div>

  <!-- Page 02 -->
  <section class="page" style="left:582px;top:18px">
    <header class="page-header"><div class="header-bar">Project Heading Here</div><div class="header-accent"></div><div class="brand"><span>Marvelund</span></div></header>
    <div class="content">
      <h2>1 Introduction</h2>
      <h3>1.1 Heading Level Two</h3>
      <p>This section gives a short overview of the project and its purpose.</p>
      <ul><li>First key point</li><li>Second key point</li><li>Third key point</li></ul>
      <h3>1.2 Scope</h3>
      <p>The scope covers planning, reporting and follow-up for all units.</p>
      <h3>1.3 Goals</h3>
      <p>Deliver a stable solution on time and within the agreed budget.</p>
      <h3>1.4 Notes</h3>
      <p class="note">Important remarks are highlighted with a yellow side rule.</p>
    </div>
    <footer class="page-footer"><span>MVL Template · Document info · Page 2</span><span class="brand">Marvelund</span></footer>
  </section>
  <div class="page-label" style="left:582px;top:350px">PAGE - 02</div>

  <!-- Page 03 Thanks -->
  <section class="page" style="left:45px;top:385px">
    <div class="thanks-top"></div>
    <div class="thanks-title">THANK YOU VERY MUCH</div>
    <div class="offices">
      <h4>Our Offices</h4>
      <div class="office"><b>Nordvik</b><br>Harbour Street 12<br>Phone +00 12 34 56 78</div>
      <div class="office"><b>Havstad</b><br>Quay Road 4<br>Phone +00 23 45 67 89</div>
      <div class="office"><b>Ekholm</b><br>Park Lane 9<br>Phone +00 34 56 78 90</div>
    </div>
    <div class="thanks-brands"><div class="brand"><span>Marvelund</span><span class="brand-dot"></span></div><div class="partner-badge"></div></div>
  </section>
  <div class="page-label" style="left:45px;top:717px">PAGE - 03</div>

  <!-- Page 04 -->
  <section class="page" style="left:313px;top:385px">
    <header class="page-header"><div class="header-bar">Project Heading Here</div><div class="header-accent"></div><div class="brand"><span>Marvelund</span></div></header>
    <div class="content">
      <p>Body text is set in a clean sans serif with open spacing for easy reading across long documents.</p>
      <p>Each page keeps the same header and footer so the document feels calm and consistent.</p>
      <p class="note">Key facts can be lifted out of the text with a short highlighted block.</p>
      <p>Paragraphs follow a steady rhythm and leave clear white space between sections.</p>
      <h2>Paragraph Title here</h2>
      <p>Use this style for new topics inside a chapter when a full heading is too strong.</p>
      <p>Tables, charts and lists follow below in the same blue palette.</p>
      <p>Keep sentences short and focus on what the reader needs to decide.</p>
    </div>
    <footer class="page-footer"><span>MVL Template · Document info · Page 4</span><span class="brand">Marvelund</span></footer>
  </section>
  <div class="page-label" style="left:313px;top:717px">PAGE - 04</div>

  <!-- Page 05 Tables -->
  <section class="page" style="left:582px;top:385px">
    <header class="page-header"><div class="header-bar">Project Heading Here</div><div class="header-accent"></div><div class="brand"><span>Marvelund</span></div></header>
    <div class="content">
      <h2>Level two title</h2>
      <p>Tables use a navy header row and light striped rows.</p>
      <h3>Table Style 1</h3>
      <table class="data-table"><tr><th>Name</th><th>Value</th><th>Value</th><th>Value</th></tr>
        <tr><td>Item A</td><td>120</td><td>140</td><td>160</td></tr>
        <tr><td>Item B</td><td>90</td><td>110</td><td>130</td></tr>
        <tr><td>Item C</td><td>75</td><td>80</td><td>95</td></tr></table>
      <h3>Table Style 2</h3>
      <table class="data-table"><tr><th>Name</th><th>Q1</th><th>Q2</th><th>Q3</th></tr>
        <tr><td>Item A</td><td>12</td><td>14</td><td>16</td></tr>
        <tr><td>Item B</td><td>9</td><td>11</td><td>13</td></tr>
        <tr><td>Item C</td><td>7</td><td>8</td><td>9</td></tr>
        <tr><td>Total</td><td>28</td><td>33</td><td>38</td></tr></table>
    </div>
    <footer class="page-footer"><span>MVL Template · Document info · Page 5</span><span class="brand">Marvelund</span></footer>
  </section>
  <div class="page-label" style="left:582px;top:717px">PAGE - 05</div>

  <!-- Page 06 Charts -->
  <section class="page" style="left:180px;top:752px">
    <header class="page-header"><div class="header-bar">Project Heading Here</div><div class="header-accent"></div><div class="brand"><span>Marvelund</span></div></header>
    <div class="content">
      <h2>Level two title</h2>
      <p>Charts follow the brand colours for clear comparison.</p>
      <h3>Graph Title</h3>
      <svg class="chart" width="202" height="72" viewBox="0 0 202 72">
        <line x1="20" y1="66" x2="190" y2="66" stroke="#c9d2db" stroke-width=".6"/>
        <rect x="40" y="36" width="16" height="30" fill="#1f5f96"/>
        <rect x="66" y="20" width="16" height="46" fill="#ee8a23"/>
        <rect x="92" y="44" width="16" height="22" fill="#0c2746"/>
        <rect x="118" y="10" width="16" height="56" fill="#2a8fb8"/>
        <rect x="144" y="30" width="16" height="36" fill="#f2b41c"/>
      </svg>
      <h3>Line chart</h3>
      <svg class="chart" width="202" height="72" viewBox="0 0 202 72">
        <g stroke="#e1e7ed" stroke-width=".5"><line x1="20" y1="10" x2="190" y2="10"/><line x1="20" y1="28" x2="190" y2="28"/><line x1="20" y1="46" x2="190" y2="46"/><line x1="20" y1="64" x2="190" y2="64"/></g>
        <polyline fill="none" stroke="#1f5f96" stroke-width="1.2" points="20,56 50,48 80,50 110,34 140,30 170,18 190,14"/>
        <polyline fill="none" stroke="#ee8a23" stroke-width="1.2" points="20,60 50,54 80,40 110,44 140,36 170,32 190,24"/>
        <polyline fill="none" stroke="#2a8fb8" stroke-width="1.2" points="20,50 50,58 80,46 110,50 140,42 170,40 190,34"/>
      </svg>
    </div>
    <footer class="page-footer"><span>MVL Template · Document info · Page 6</span><span class="brand">Marvelund</span></footer>
  </section>
  <div class="page-label" style="left:180px;top:1084px">PAGE - 06</div>

  <!-- Back page -->
  <section class="page back" style="left:447px;top:752px">
    <div class="section-break">
      <div class="rule"></div>
      <h1>SECTION BREAK TITLE HERE</h1>
      <p>A short line of supporting text introduces the next part of the document.</p>
    </div>
  </section>
  <div class="page-label" style="left:447px;top:1084px">BACK PAGE</div>

</div>
</body>
</html>
```